Pirokalme war genau die Richtige für mich. Sie hat zügig und professionell gearbeitet und ihr Entwurf hat genau meinen Geschmack getroffen. Die Kommunikation war sehr freundlich und klar.
Zielgruppe
Ich bin Systemische Coach und möchte eine Methode bewerben. Es geht dabei um Auflösung von Schocktraumata. Also Trauma nach Unfall, Gewalterfahrung, Katastrophe, Diagnose, Operation, traumatischer Geburt, etc.
Mein Flyer soll Menschen erreichen, die so etwas erlebt haben und bei denen das Ereignis immer noch getriggert wird. z.B. Polizist:innen, Rettungshelfer:innen, Ärzt:innen
Genaueres hier: www.ruhe-anker.de
Die Methode bietet schnelle Hilfe, arbeitet mit Visualisierung und Klopfen, und retraumatisiert nicht.
Aufgabenstellung
Design sollte sich an der Website orientieren. Texte können davon genommen werden.
Anbei noch ein Text, der in einem Veranstaltungsnewsletter erscheint.
Bildmaterial ebenfalls von Website (bitte dann anfragen, was gebraucht wird) oder sehr gerne auch anderes von bilder.velmora.com
Format: Din lang, 4 Seiten, hoch oder quer ist egal

```html
<!DOCTYPE html>
<html lang="de">
<head>
<meta charset="utf-8">
<title>Flyer Ruhe-Anker – Innenseiten</title>
<link href="https://fonts.googleapis.com/css2?family=Open+Sans:wght@400;600;700&family=Handlee&display=swap" rel="stylesheet">
<style>
  :root {
    --page-bg: #e9e9eb;
    --paper: #f3f3f4;
    --indigo: #4a4f9d;
    --indigo-light: #6667ad;
    --indigo-pale: #c9c9e6;
    --text: #222228;
    --white: #ffffff;
  }
  * { box-sizing: border-box; margin: 0; padding: 0; }
  html, body { width: 1119px; height: 1200px; overflow: hidden; }
  body {
    background: var(--page-bg);
    font-family: "Open Sans", Arial, sans-serif;
    color: var(--text);
  }
  .spread {
    position: absolute; left: 41px; top: 20px;
    width: 1037px; height: 1160px;
    display: flex;
    background: var(--paper);
  }
  .panel { position: relative; height: 100%; overflow: hidden; background: var(--paper); }
  .panel--left { width: 539px; }
  .panel--right { width: 498px; }

  /* left panel */
  .top-band { position: absolute; left: 0; top: 0; width: 100%; height: 247px; background: var(--indigo); }
  .top-band__accent { position: absolute; left: 400px; top: 0; width: 139px; height: 247px; background: var(--indigo-light); }
  .consult-photo {
    position: absolute; left: 27px; top: 25px; width: 485px; height: 268px;
    background: linear-gradient(100deg, #d9c6a8 0%, #efe8df 30%, #f7f4ef 55%, #cdb9a2 80%, #e9dccb 100%);
  }
  .intro { position: absolute; left: 49px; top: 340px; width: 441px; }
  .intro h2 { font-size: 21px; font-weight: 600; color: var(--indigo); margin-bottom: 10px; }
  .intro p {
    font-size: 17.3px; line-height: 24.3px; text-align: justify; hyphens: auto;
    margin-bottom: 11px;
  }
  .intro .lead, .intro .conclusion { font-weight: 600; color: var(--indigo); }

  .bottom-band { position: absolute; left: 0; bottom: 0; width: 100%; height: 68px; background: var(--indigo); }
  .bottom-band__accent { position: absolute; left: 400px; top: 0; width: 139px; height: 38px; background: var(--indigo-light); }

  /* right panel */
  .top-rule { position: absolute; left: 0; top: 0; width: 100%; height: 5px; background: var(--indigo-pale); }
  .question { position: absolute; left: 49px; top: 60px; width: 400px; }
  .question h2 { font-size: 20px; line-height: 26px; font-weight: 600; color: var(--indigo); margin-bottom: 10px; }
  .question p { font-size: 16.4px; line-height: 23.5px; text-align: justify; hyphens: auto; }
  .sunset-photo {
    position: absolute; left: 0; top: 360px; width: 100%; height: 732px;
    border-top: 4px solid var(--indigo-light);
    background: linear-gradient(180deg, #b9bcc4 0%, #cdbfae 25%, #e7b778 50%, #f2c46c 68%, #b87a3e 82%, #4a3222 100%);
  }
  .quote {
    position: absolute; right: 54px; top: 748px; width: 320px;
    font-family: "Handlee", cursive; color: var(--indigo);
    font-size: 22px; line-height: 38px; text-align: right;
  }
  .quote p + p { margin-top: 6px; }
  .quote cite { display: block; font-family: "Open Sans", Arial, sans-serif; font-style: normal; font-size: 16px; line-height: 24px; }
  .url-band {
    position: absolute; left: 0; bottom: 0; width: 100%; height: 68px;
    background: var(--indigo); color: var(--white);
    display: flex; align-items: center; justify-content: center;
    font-size: 22px; font-weight: 700;
  }
</style>
</head>
<body>
<main class="spread">
  <section class="panel panel--left">
    <div class="top-band"><div class="top-band__accent"></div></div>
    <div class="consult-photo" role="img" aria-label="Foto: Beratungsgespräch zwischen zwei Frauen in einem hellen Raum"></div>
    <article class="intro">
      <h2>Haben Sie ein Trauma?</h2>
      <p class="lead">Sie haben Schlimmes erlebt und es sitzt Ihnen noch in den Knochen, hängt Ihnen nach, holt Sie ein, triggert Sie…? Sie erleben Albträume, Flashbacks, fühlen sich blockiert, verletzt, gebremst, beschämt, schuldig, überschattet, wie im Nebel, zerbrochen…?</p>
      <p>Egal, wie „groß“ oder „klein“ die Verletzung (griechisch: Trauma) war, lassen Sie nicht zu, dass sie Ihr Leben bestimmt, Sie beeinträchtigt, Sie davon abhält, Dinge zu tun, die Sie gerne tun würden.</p>
      <p>Sie brauchen nicht darauf zu warten, dass „die Zeit alle Wunden heilt“… Sie können jetzt sofort etwas tun, um die Verbindung zwischen dem Ereignis und den Mustern zu entkoppeln, die automatisch im Gehirn und Körper gestartet werden, sobald Sie etwas daran erinnert, es also einen Auslöser oder Trigger gibt.</p>
      <p>Dies gelingt mit der Anwendung der Ruhe-Anker-Technik – einer Methode, die durch eine Kombination aus Klopf-Akupressur und auditiv-visuellen-motorischen Reizen neuronale Veränderungen im Gehirn bewirkt. Neuronale Muster, die durch das Trauma entstanden sind, werden gelöst und neu konditioniert.</p>
      <p class="conclusion">Das Geschehene wird zu einer normalen Erinnerung und löst keine Symptome mehr aus.</p>
    </article>
    <div class="bottom-band"><div class="bottom-band__accent"></div></div>
  </section>

  <section class="panel panel--right">
    <div class="top-rule"></div>
    <article class="question">
      <h2>Haben Sie schon mal etwas erlebt, das tiefe Spuren in Ihrer Psyche hinterlassen hat?</h2>
      <p>Ein Ereignis, in dessen Situation Sie sich ausgeliefert fühlten? Das kann ein Unfall sein, irgendeine Art von Operation, eine schlimme Diagnose, ein Todesfall, Untreue, Trennung, Scheidung, schlechte Nachrichten, erlebte Gewalt. Wenn man selbst betroffen ist, aber auch, wenn man Zeuge/Zuschauer des Ereignisses wurde.</p>
    </article>
    <div class="sunset-photo" role="img" aria-label="Foto: Frau als Silhouette im Sonnenuntergang, die Arme erhoben, Vögel fliegen davon"></div>
    <blockquote class="quote">
      <p>Dass die Vögel der Sorge und des Kummers über deinem Haupt fliegen, kannst du nicht ändern.</p>
      <p>Doch du kannst verhindern, dass sie Nester in deinem Haar bauen.</p>
      <cite>(Jorin Haldeck)</cite>
    </blockquote>
    <div class="url-band">www.ruhe-anker.de</div>
  </section>
</main>
</body>
</html>
```